Ad designs for TalkHive and Lumora

We are a company that buy and sell airlines miles.
We publish our Ads on TH and Lumora and wish to receive 10 designs that reflects our business with some texts. Please see some examples.
10 designs with includes some text in English and those same 10 designs with include a text in Hebrew (written from right to left).
We need each of the designs to eventually be created at the following ratios and resolutions:
Square format (1:1): 1080 x 1080 pixels
Vertical format (9:16): 1080 x 1920 pixels
Horizontal format (16:9): 1280 x 720 pixels
Vertical video format (4:5): 1080 x 1350 pixels
Please see the samples sent and our login as well attached
Texts in English:
"We buy your airline miles for"
or
"Sell us your airline miles"
or
"Receive money for your airline miles"

and in Hebrew:
"אנחנו קונים את הנקודות שלכם בחברות התעופה"
or
"קונים נקודות נוסע מתמיד תמורת מזומן"
or
"קונים נקודות טל גן וחברות אחרות"

Please add a red button to all Ads in Eng saying "Get Quote"
and in Heb saying "להצעת מחיר"

```html
<!DOCTYPE html>
<html lang="en">
<head>
<meta charset="utf-8">
<title>Airline Miles Ads</title>
<link rel="stylesheet" href="https://fonts.googleapis.com/css2?family=Jost:wght@500;600&family=Montserrat:wght@800&family=Assistant:wght@400;600&display=swap">
<style>
  :root {
    --board: #dcdcdc;
    --white: #ffffff;
    --ink: #1c1c1c;
    --edge: #9a9a9a;
    --red-top: #7a0006;
    --red-mid: #c00010;
    --red-bright: #e5121c;
    --photo-dark: #2a1608;
    --photo-mid: #6e4219;
    --photo-warm: #b98a45;
    --photo-light: #e6cd95;
  }
  * { margin: 0; padding: 0; box-sizing: border-box; }
  html, body {
    width: 1200px; height: 959px; overflow: hidden;
    background: var(--board);
  }
  .board { position: relative; width: 1200px; height: 959px; }

  .ad {
    position: absolute;
    background: var(--white);
    border: 1px solid var(--edge);
    overflow: hidden;
  }
  .ad--story { left: 56px; top: 9px; width: 519px; height: 922px; }
  .ad--square { left: 628px; top: 185px; width: 519px; height: 519px; }

  .ad__photo {
    position: absolute; left: 0; top: 0; width: 100%;
    background:
      radial-gradient(ellipse 60% 40% at 75% 12%, rgba(240,215,160,.75), transparent 70%),
      radial-gradient(ellipse 50% 45% at 90% 60%, rgba(200,150,90,.55), transparent 70%),
      linear-gradient(115deg, var(--photo-dark) 0%, var(--photo-mid) 35%, var(--photo-dark) 55%, var(--photo-warm) 80%, var(--photo-light) 100%);
  }
  .ad--story .ad__photo { height: 765px; }
  .ad--square .ad__photo { height: 470px; }

  .ad__curve { position: absolute; left: 0; width: 100%; display: block; }
  .ad--story .ad__curve { top: 700px; height: 70px; }
  .ad--square .ad__curve { top: 410px; height: 60px; }

  .ad__headline {
    position: absolute; left: 0; width: 100%;
    text-align: center;
    font-family: 'Jost', sans-serif; font-weight: 600;
    color: var(--white);
    line-height: 1.0;
    text-shadow: 0 2px 8px rgba(0,0,0,.35);
  }
  .ad--story .ad__headline { top: 308px; font-size: 45px; }
  .ad--square .ad__headline { top: 28px; font-size: 48px; line-height: 0.95; }

  .ad__subline {
    position: absolute; left: 0; width: 100%;
    text-align: center;
    font-family: 'Assistant', sans-serif; font-weight: 400;
    color: var(--white);
    direction: rtl;
    text-shadow: 0 2px 6px rgba(0,0,0,.35);
  }
  .ad--story .ad__subline { top: 420px; font-size: 29px; }
  .ad--square .ad__subline { top: 140px; font-size: 28px; }

  .cta {
    position: absolute;
    display: flex; align-items: center; justify-content: center;
    border-radius: 999px;
    background: linear-gradient(180deg, var(--red-top) 0%, var(--red-mid) 55%, var(--red-bright) 100%);
    box-shadow: inset 0 0 0 2px rgba(255,60,60,.6), 0 2px 6px rgba(0,0,0,.25);
    color: var(--white);
  }
  .cta__label { text-align: center; line-height: 0.95; }
  .cta__en { font-family: 'Montserrat', sans-serif; font-weight: 800; letter-spacing: .5px; display: block; }
  .cta__he { font-family: 'Assistant', sans-serif; font-weight: 600; direction: rtl; display: block; }
  .cta__arrows { margin-left: 12px; display: block; }

  .ad--story .cta { left: 129px; top: 504px; width: 247px; height: 73px; }
  .ad--story .cta__en { font-size: 23px; }
  .ad--story .cta__he { font-size: 27px; }
  .ad--story .cta__arrows { width: 40px; height: 22px; }

  .ad--square .cta { left: 286px; top: 443px; width: 195px; height: 57px; }
  .ad--square .cta__en { font-size: 18px; }
  .ad--square .cta__he { font-size: 21px; }
  .ad--square .cta__arrows { width: 32px; height: 18px; }

  .brand {
    position: absolute;
    font-family: 'Jost', sans-serif; font-weight: 500;
    color: var(--ink);
    letter-spacing: .5px;
    white-space: nowrap;
  }
  .ad--story .brand { left: 0; width: 100%; text-align: center; top: 795px; font-size: 22px; }
  .ad--square .brand { left: 26px; top: 469px; font-size: 19px; }
</style>
</head>
<body>
<div class="board">

  <section class="ad ad--story">
    <div class="ad__photo" role="img" aria-label="Traveller holding a passport with boarding passes in a blurred airport terminal"></div>
    <svg class="ad__curve" viewBox="0 0 519 70" preserveAspectRatio="none" aria-hidden="true">
      <path d="M0 14 Q260 90 519 12 L519 70 L0 70 Z" fill="#ffffff"/>
    </svg>
    <h1 class="ad__headline">Receive money for<br>your airline miles</h1>
    <p class="ad__subline">קונים נקודות טל גן וחברות אחרות</p>
    <a class="cta">
      <span class="cta__label"><span class="cta__en">GET QUOTE</span><span class="cta__he">להצעת מחיר</span></span>
      <svg class="cta__arrows" viewBox="0 0 40 22" aria-hidden="true" fill="none" stroke-width="3" stroke-linecap="round" stroke-linejoin="round">
        <path d="M2 2 L10 11 L2 20" stroke="#ff2a2a"/>
        <path d="M11 2 L19 11 L11 20" stroke="#ff4a4a"/>
        <path d="M20 2 L28 11 L20 20" stroke="#ff7070"/>
        <path d="M29 2 L37 11 L29 20" stroke="#ff9a9a"/>
      </svg>
    </a>
    <div class="brand">MILO SKY</div>
  </section>

  <section class="ad ad--square">
    <div class="ad__photo" role="img" aria-label="Traveller holding a passport with boarding passes in a blurred airport terminal"></div>
    <svg class="ad__curve" viewBox="0 0 519 60" preserveAspectRatio="none" aria-hidden="true">
      <path d="M0 10 Q230 75 519 8 L519 60 L0 60 Z" fill="#ffffff"/>
    </svg>
    <h1 class="ad__headline">Receive money for<br>your airline miles</h1>
    <p class="ad__subline">קונים נקודות טל גן וחברות אחרות</p>
    <div class="brand">MILO SKY</div>
    <a class="cta">
      <span class="cta__label"><span class="cta__en">GET QUOTE</span><span class="cta__he">להצעת מחיר</span></span>
      <svg class="cta__arrows" viewBox="0 0 40 22" aria-hidden="true" fill="none" stroke-width="3" stroke-linecap="round" stroke-linejoin="round">
        <path d="M2 2 L10 11 L2 20" stroke="#ff2a2a"/>
        <path d="M11 2 L19 11 L11 20" stroke="#ff4a4a"/>
        <path d="M20 2 L28 11 L20 20" stroke="#ff7070"/>
        <path d="M29 2 L37 11 L29 20" stroke="#ff9a9a"/>
      </svg>
    </a>
  </section>

</div>
</body>
</html>
```